Biz card for my counselling/social work practice

Biz card design for my counselling practice, focus on well-being, I am a social worker who also teaches meditation and workshops but my main focus for the card is my counselling practice. My website reveals a gentle flowing quality which I would life reflected in my card. This business card will be designed to share with other practitioners who are looking for support with their clients to take their healing to another level or well-being.

Target Market(s)

professionals seeking mental health counselling/men/women/ those seeking to improve their well-being through insight based counselling to optimize their lives and process trauma or limiting patterns

Industry/Entity Type

Counsellor

Contact Information for Business Card

Info on the card: perhaps text is aligned left?
Marla Finch, MSW, RSW
Counsellor
250.555.0142
info@marlafinch.ca
www.marlafinch.ca

Please use a modern font doesn’t need to be the one chosen below. Thank you

Font styles to use
Serif

Colors
3176b5
33a6d7
33b8a4
6b449b
abd037
d2a4cc
e55fa2

Requirements
Must have
• My business card details on front
• Backside
• Accelerated Resolution Therapy
• Cognitive Behavioral Therapy
• Mindfulness Informed Therapy
Nice to have
• I would like the card to be basic, (white or creme without too much bold colour) and with perhaps a stripe or band of vertical colour in blue or green (or a merge of colour) perhaps embossed or in a negative space. (this is one idea, but do not want the card to be too feminine or interest only women as i see men too so this is only an idea, but not 100 percent on this.
• I do not have a logo. I would prefer to heart from my website not to be used in the design as i am considering modifying this and re-branding.
Should not have
• too bold colours or bright yellow/blacks. i Like tones that are greens, blues.

```html
<!DOCTYPE html>
<html lang="en">
<head>
<meta charset="utf-8">
<title>Marla Finch — Counsellor business card</title>
<link rel="stylesheet" href="https://fonts.googleapis.com/css2?family=Quicksand:wght@400;500;700&display=swap">
<style>
  :root {
    --bg: #a9d6c6;
    --paper: #f1f0ed;
    --edge: #bfe9e0;
    --green: #1f9d86;
    --blue: #2a68b0;
    --shadow: rgba(40, 90, 75, 0.28);
  }
  * { box-sizing: border-box; margin: 0; padding: 0; }
  html, body {
    width: 1200px; height: 818px; overflow: hidden;
    background: var(--bg);
    font-family: "Quicksand", sans-serif;
  }
  .stage {
    width: 1200px; height: 818px;
    display: flex; align-items: center; justify-content: center; gap: 50px;
  }
  .card {
    position: relative;
    width: 540px; height: 309px;
    background: var(--paper);
    border-bottom: 4px solid var(--edge);
    box-shadow: 0 14px 30px var(--shadow);
  }
  .card__art { position: absolute; inset: 0; width: 100%; height: 100%; }

  /* Front */
  .identity {
    position: absolute; top: 34px; right: 58px;
    text-align: right; line-height: 1.15;
  }
  .identity__name { font-size: 25px; font-weight: 700; color: var(--green); }
  .identity__creds { font-size: 21px; font-weight: 400; color: var(--green); }
  .identity__role { font-size: 20px; font-weight: 500; color: var(--blue); }
  .contact {
    position: absolute; top: 132px; right: 62px;
    list-style: none; text-align: right;
    color: var(--blue); font-size: 18px; font-weight: 500; line-height: 1.6;
  }

  /* Back */
  .services {
    position: absolute; top: 92px; right: 70px;
    list-style: none; text-align: right;
    color: var(--blue); font-size: 24px; font-weight: 500; line-height: 1.65;
  }
</style>
</head>
<body>
<main class="stage">

  <section class="card card--front" aria-label="Business card front">
    <svg class="card__art" viewBox="0 0 540 309" aria-hidden="true">
      <rect class="accent-bar" x="500" y="38" width="9" height="60" fill="#1f9d86"/>
      <!-- contact rail -->
      <polyline points="510,128 510,272 60,272" fill="none" stroke="#1f9d86" stroke-width="3"/>
      <line x1="500" y1="128" x2="520" y2="128" stroke="#1f9d86" stroke-width="3"/>
      <g fill="#2a68b0">
        <circle cx="510" cy="146" r="9"/>
        <circle cx="510" cy="175" r="9"/>
        <circle cx="510" cy="204" r="9"/>
        <circle cx="86" cy="272" r="11"/>
      </g>
      <!-- phone -->
      <path d="M506 141 q-1 5 4 10 q5 5 10 4 l-1-3 -3 0 -2-2 0-3z" fill="#f1f0ed" transform="translate(-4,-2) scale(1)"/>
      <!-- mail -->
      <rect x="504.5" y="171" width="11" height="8" fill="none" stroke="#f1f0ed" stroke-width="1.3"/>
      <polyline points="504.5,171 510,176 515.5,171" fill="none" stroke="#f1f0ed" stroke-width="1.3"/>
      <!-- web -->
      <circle cx="510" cy="204" r="5.5" fill="none" stroke="#f1f0ed" stroke-width="1.2"/>
      <ellipse cx="510" cy="204" rx="2.4" ry="5.5" fill="none" stroke="#f1f0ed" stroke-width="1"/>
      <line x1="504.5" y1="204" x2="515.5" y2="204" stroke="#f1f0ed" stroke-width="1"/>
    </svg>
    <header class="identity">
      <p><span class="identity__name">Marla Finch</span><span class="identity__creds">, MSW, RSW</span></p>
      <p class="identity__role">Counsellor</p>
    </header>
    <ul class="contact">
      <li>250.555.0142</li>
      <li>info@marlafinch.ca</li>
      <li>www.marlafinch.ca</li>
    </ul>
  </section>

  <section class="card card--back" aria-label="Business card back">
    <svg class="card__art" viewBox="0 0 540 309" aria-hidden="true">
      <line x1="505" y1="22" x2="505" y2="288" stroke="#1f9d86" stroke-width="3"/>
      <g fill="#2a68b0">
        <circle cx="505" cy="112" r="10"/>
        <circle cx="505" cy="150" r="10"/>
        <circle cx="505" cy="188" r="10"/>
      </g>
    </svg>
    <ul class="services">
      <li>Accelerated Resolution Therapy</li>
      <li>Cognitive Behavioral Therapy</li>
      <li>Mindfulness Informed Therapy</li>
    </ul>
  </section>

</main>
</body>
</html>
```